Banner

I need a banner made showcasing our products and USPs! I have attached a design that was done in-house but not very good so looking for a better design

Industry/Entity Type

Fintech

```html
<!DOCTYPE html>
<html lang="en">
<head>
<meta charset="utf-8">
<title>ClearTill Merchant Services Banner</title>
<link rel="stylesheet" href="https://fonts.googleapis.com/css2?family=Open+Sans:wght@400;600;700;800&display=swap">
<style>
  :root {
    --navy: #2b4f8c;
    --band-blue: #2e5591;
    --band-dark: #243a63;
    --orange: #e08a1c;
    --badge-orange: #e3a037;
    --badge-rim: #eebf6e;
    --grey-text: #6b6b6b;
    --page-bg: #eef0f2;
    --white: #ffffff;
  }
  * { box-sizing: border-box; margin: 0; padding: 0; }
  html, body { width: 1200px; height: 923px; overflow: hidden; background: var(--page-bg); }
  body { font-family: "Open Sans", Arial, sans-serif; position: relative; }

  .banner {
    position: absolute; left: 370px; top: 11px;
    width: 460px; height: 900px; background: var(--white); overflow: hidden;
  }
  .banner-shapes { position: absolute; inset: 0; }

  .brand { position: absolute; left: 24px; top: 22px; width: 330px; }
  .brand-name {
    font-weight: 700; font-size: 74px; line-height: 84px; color: var(--navy); letter-spacing: -1px;
  }
  .brand-sub {
    position: absolute; left: 98px; top: 82px;
    font-size: 21px; color: var(--grey-text); white-space: nowrap;
  }
  .brand-mark {
    position: absolute; left: 353px; top: 41px; width: 80px; height: 80px;
    border-radius: 50%; background: var(--navy);
  }

  .tagline {
    position: absolute; left: 34px; top: 140px;
    font-size: 38px; line-height: 40px; color: var(--navy); font-weight: 400;
  }

  .offer-badge {
    position: absolute; left: 22px; top: 359px; width: 172px; height: 172px;
    border-radius: 50%; background: var(--badge-orange); border: 4px solid var(--badge-rim);
    color: var(--white); text-align: center; font-weight: 700;
    display: flex; flex-direction: column; justify-content: center;
  }
  .offer-badge .small { font-size: 17px; line-height: 20px; }
  .offer-badge .big { font-size: 40px; line-height: 40px; font-weight: 800; }

  .usp-panel {
    position: absolute; left: 232px; top: 236px; width: 216px; height: 320px;
    background: rgba(255,255,255,0.72); border-radius: 10px;
  }
  .usp {
    position: absolute; left: 42px; font-size: 15px; line-height: 22px;
    font-weight: 700; color: var(--navy); text-transform: uppercase;
  }
  .usp::before {
    content: ""; position: absolute; left: -38px; top: 50%; width: 28px; height: 28px;
    margin-top: -14px; border: 2px solid var(--orange); border-radius: 50%;
  }
  .usp::after {
    content: ""; position: absolute; left: -29px; top: 50%; width: 8px; height: 14px;
    margin-top: -10px; border: solid var(--orange); border-width: 0 3px 3px 0; transform: rotate(40deg);
  }

  .product { position: absolute; top: 638px; width: 120px; }
  .product-photo {
    width: 94px; height: 94px; border-radius: 50%; border: 3px solid var(--white); margin-left: 2px;
  }
  .product-label {
    margin-top: 8px; padding-left: 6px; border-left: 2px solid var(--white);
    color: var(--white); font-size: 14px; line-height: 19px; font-weight: 600; text-transform: uppercase;
  }

  .accept-strip {
    position: absolute; left: 0; right: 0; top: 872px;
    display: flex; justify-content: center; gap: 14px;
  }
  .accept-strip span {
    font-size: 13px; line-height: 18px; font-weight: 600; color: var(--navy);
  }
</style>
</head>
<body>
  <div class="banner">
    <svg class="banner-shapes" width="460" height="900" viewBox="0 0 460 900">
      <defs>
        <linearGradient id="crowd" x1="0" y1="0" x2="1" y2="1">
          <stop offset="0" stop-color="#d9d4cc"/>
          <stop offset="0.5" stop-color="#c8c2b8"/>
          <stop offset="1" stop-color="#8f8a86"/>
        </linearGradient>
      </defs>
      <polygon points="0,310 460,210 460,545 0,630" fill="url(#crowd)" role="img" aria-label="Photo of a cheering group of business people"/>
      <polygon points="0,630 460,545 460,813 0,813" fill="var(--band-blue)"/>
      <rect x="0" y="813" width="460" height="22" fill="var(--band-dark)"/>
    </svg>

    <div class="brand">
      <div class="brand-name">ClearTill</div>
      <div class="brand-sub">Merchant Services</div>
    </div>
    <div class="brand-mark"></div>

    <h1 class="tagline">innovative<br>payment<br>solutions</h1>

    <div class="offer-badge">
      <div class="small">WE</div>
      <div class="small">WILL BEAT</div>
      <div class="big">ANY</div>
      <div class="small">LIKE FOR LIKE</div>
      <div class="small">QUOTE</div>
    </div>

    <div class="usp-panel">
      <div class="usp" style="top:14px">Same day/next day<br>funding</div>
      <div class="usp" style="top:76px">24 hour<br>swap-out</div>
      <div class="usp" style="top:139px">Tapwise &amp;<br>Lumo Wallet<br>enabled</div>
      <div class="usp" style="top:224px">Integrated<br>EPOS solution</div>
      <div class="usp" style="top:286px">Save up to 40%</div>
    </div>

    <div class="product" style="left:48px">
      <div class="product-photo" role="img" aria-label="Card terminal with a card being inserted" style="background:linear-gradient(135deg,#e8e8e8,#3a3a3a)"></div>
      <div class="product-label">Card<br>payments</div>
    </div>
    <div class="product" style="left:182px">
      <div class="product-photo" role="img" aria-label="Fanned banknotes" style="background:linear-gradient(135deg,#efe4cf,#b9a27a)"></div>
      <div class="product-label">Cash<br>advance</div>
    </div>
    <div class="product" style="left:317px">
      <div class="product-photo" role="img" aria-label="Till screen and desk phone" style="background:linear-gradient(135deg,#f4f6f8,#5b6470)"></div>
      <div class="product-label">EPOS<br>systems</div>
    </div>

    <div class="accept-strip">
      <span>Lumo Wallet</span><span>Norvane</span><span>Kestrel</span><span>Plenta</span><span>Quillo</span><span>Zephra</span><span>Tapwise</span>
    </div>
  </div>
</body>
</html>
```